Profesional personal website needs design and business card

I need a business card with my professional name as a logo "Marlo Vitality" for my business. I am a Wellness Coach, consultant and trainer. So it should be professional, wellness oriented and modern.

Target Market(s)

Private clients, governments, corporations. Luxury and high market.

Industry/Entity Type

Health And Wellness

Contact Information for Business Card

Marlo Vitality should be the logo

Colors

Designer to choose colors to be used in the design.

Requirements
Must have
• Marlo Vitality
• Name: Tomás Arribal
• Wellness Coach, Consultant & Trainer.
• Website: www.marlovitality.example
• Phone:
• Spain (+34) 612 480 397
• (USA) +1 (555) 318 2046
Nice to have
• The most important is the design of "Marlo Vitality", as this is going to be my personal brand logo. It should be professional, wellness, high end and actual.
Should not have
• no golds, no baroque style..

```html
<!DOCTYPE html>
<html lang="en">
<head>
<meta charset="utf-8">
<title>Marlo Vitality – Business Card</title>
<link href="https://fonts.googleapis.com/css2?family=Lato:wght@400&display=swap" rel="stylesheet">
<style>
  :root {
    --card-navy: #1b3d4f;
    --accent-teal: #2fa9c4;
    --swirl-teal: #3a8ea4;
    --ink-white: #ffffff;
    --bg-top: #f5f5f7;
    --bg-bottom: #b5dce4;
  }
  * { margin: 0; padding: 0; box-sizing: border-box; }
  html, body {
    width: 1200px;
    height: 1200px;
    overflow: hidden;
  }
  body {
    position: relative;
    background: linear-gradient(180deg, var(--bg-top) 0%, var(--bg-bottom) 100%);
    font-family: "Lato", sans-serif;
    color: var(--ink-white);
  }
  .card {
    position: absolute;
    left: 192px;
    width: 816px;
    height: 466px;
    background: var(--card-navy);
    overflow: hidden;
    box-shadow: 0 6px 18px rgba(20, 50, 65, 0.22);
  }
  .card--front { top: 94px; }
  .card--back { top: 640px; }

  .decor-field {
    position: absolute;
    top: 0;
    bottom: 0;
    right: 0;
  }
  .card--front .decor-field {
    width: 420px;
    background:
      radial-gradient(ellipse 55% 40% at 55% 38%, rgba(58, 168, 191, 0.30) 0%, rgba(58, 168, 191, 0) 70%),
      radial-gradient(ellipse 40% 70% at 30% 60%, rgba(58, 142, 164, 0.22) 0%, rgba(58, 142, 164, 0) 70%);
  }
  .card--back .decor-field {
    width: 400px;
    background:
      radial-gradient(ellipse 50% 35% at 45% 22%, rgba(58, 142, 164, 0.22) 0%, rgba(58, 142, 164, 0) 70%),
      radial-gradient(ellipse 45% 45% at 65% 70%, rgba(58, 168, 191, 0.26) 0%, rgba(58, 168, 191, 0) 70%);
  }

  .brand {
    position: absolute;
    display: flex;
    align-items: center;
  }
  .card--front .brand { left: 52px; top: 148px; }
  .card--back .brand { left: 258px; top: 28px; }
  .brand-mark {
    width: 26px;
    height: 26px;
    border-radius: 50%;
    background: var(--accent-teal);
    flex: none;
    margin-right: 20px;
  }
  .brand-name {
    font-weight: 400;
    font-size: 68px;
    line-height: 1;
    letter-spacing: 1px;
    color: var(--ink-white);
  }
  .brand-name .line { display: block; }
  .brand-name .line--second { padding-left: 40px; margin-top: 6px; }

  .holder {
    position: absolute;
    left: 28px;
    top: 208px;
    font-size: 25px;
    line-height: 30px;
  }

  .contact-list {
    position: absolute;
    left: 28px;
    top: 280px;
    list-style: none;
  }
  .contact-item {
    display: flex;
    align-items: center;
    height: 33px;
    margin-bottom: 11px;
    font-size: 25px;
  }
  .contact-icon {
    width: 33px;
    height: 33px;
    flex: none;
    margin-right: 32px;
  }
</style>
</head>
<body>

  <section class="card card--front" aria-label="Business card front">
    <div class="decor-field" role="img" aria-label="Large faint teal flourish decoration"></div>
    <div class="brand">
      <span class="brand-mark" aria-hidden="true"></span>
      <div class="brand-name">
        <span class="line">Marlo</span>
        <span class="line line--second">Vitality</span>
      </div>
    </div>
  </section>

  <section class="card card--back" aria-label="Business card back">
    <div class="decor-field" role="img" aria-label="Large faint teal flourish decoration"></div>
    <div class="brand">
      <span class="brand-mark" aria-hidden="true"></span>
      <div class="brand-name">
        <span class="line">Marlo</span>
        <span class="line line--second">Vitality</span>
      </div>
    </div>

    <div class="holder">
      <p class="holder-name">Tomás Arribal</p>
      <p class="holder-role">Wellness Coach, Consultant &amp; Trainer</p>
    </div>

    <ul class="contact-list">
      <li class="contact-item">
        <svg class="contact-icon" viewBox="0 0 32 32" aria-hidden="true">
          <circle cx="16" cy="16" r="16" fill="#fff"/>
          <path d="M10.5 8.5c1-.8 2-.6 2.6.3l1.4 2.3c.5.8.3 1.6-.4 2.2l-.9.7c.8 2 2.6 4 4.6 5l.8-.9c.6-.7 1.5-.8 2.2-.3l2.3 1.5c.8.6.9 1.6.2 2.5-1.3 1.7-3.2 2.2-5.4 1-3.5-1.9-6.3-4.9-7.9-8.5-.9-2.2-.7-4.4.5-5.8z" fill="none" stroke="#1b3d4f" stroke-width="1.6" stroke-linejoin="round"/>
        </svg>
        <span>Spain: (+34) 612 480 397</span>
      </li>
      <li class="contact-item">
        <svg class="contact-icon" viewBox="0 0 32 32" aria-hidden="true">
          <circle cx="16" cy="16" r="16" fill="#fff"/>
          <path d="M10.5 8.5c1-.8 2-.6 2.6.3l1.4 2.3c.5.8.3 1.6-.4 2.2l-.9.7c.8 2 2.6 4 4.6 5l.8-.9c.6-.7 1.5-.8 2.2-.3l2.3 1.5c.8.6.9 1.6.2 2.5-1.3 1.7-3.2 2.2-5.4 1-3.5-1.9-6.3-4.9-7.9-8.5-.9-2.2-.7-4.4.5-5.8z" fill="none" stroke="#1b3d4f" stroke-width="1.6" stroke-linejoin="round"/>
        </svg>
        <span>USA: +1 (555) 318 2046</span>
      </li>
      <li class="contact-item">
        <svg class="contact-icon" viewBox="0 0 32 32" aria-hidden="true">
          <circle cx="16" cy="16" r="16" fill="#fff"/>
          <circle cx="16" cy="16" r="8.5" fill="none" stroke="#1b3d4f" stroke-width="1.6"/>
          <ellipse cx="16" cy="16" rx="3.8" ry="8.5" fill="none" stroke="#1b3d4f" stroke-width="1.3"/>
          <line x1="7.5" y1="16" x2="24.5" y2="16" stroke="#1b3d4f" stroke-width="1.3"/>
        </svg>
        <span>www.marlovitality.example</span>
      </li>
    </ul>
  </section>

</body>
</html>
```